Vexel Business Cards

We need a new look business cvard to refelect our new look website www.vexel-example.com.au
We’re Vexel, a team of town planning and traffic and transport engineering specialists located in Melbourne.

Vexel is a company that is structured, articulate, dynamic, progressive, accurate and adaptable.
Our key messages are:
1. We make your life easier by doing what we do best
2. We tell you what you need to know not what you want to hear
3. Polished and professional but not afraid to show some personality

we would like a bold new look that is polished and professional but not afraid to show a bit of personality

Target Market(s)

Vexel’s diverse client base consists of architecture practices, builders, developers, local government and the legal fraternity.

Industry/Entity Type

Town

Requirements
Must have
• must use our logo and have the following information

Joel Harcastle
Director

Vexel Consultants Pty Ltd
Fernhollow first floor
Tamber Street
Elmsworth VIC 3988 Australia
+61 03 9555 0187
mail@vexel-example.com.au
www.vexel-example.com.au
Nice to have
• We would like to see the logo used or the colours of the logo used.

```html
<!DOCTYPE html>
<html lang="en">
<head>
<meta charset="utf-8">
<title>Vexel Business Cards</title>
<link rel="stylesheet" href="https://fonts.googleapis.com/css2?family=Source+Sans+3:wght@400;600;700&display=swap">
<style>
  :root {
    --backdrop: #141414;
    --card: #e6e7e8;
    --ink: #4d5560;
    --ink-soft: #5f6670;
    --accent-blue: #1fa4dc;
    --tile-blue: #2a9fd6;
    --tile-blue-deep: #1a6fb0;
    --tile-green: #5bb55a;
    --tile-green-deep: #2f8a3a;
    --tile-grey: #9a9a9a;
  }
  * { margin: 0; padding: 0; box-sizing: border-box; }
  html, body {
    width: 1200px; height: 849px; overflow: hidden;
    background: var(--backdrop);
    font-family: "Source Sans 3", "Myriad Pro", Arial, sans-serif;
  }
  .stage { position: relative; width: 1200px; height: 849px; }
  .card {
    position: absolute; top: 337px;
    width: 366px; height: 224px;
    background: var(--card);
    overflow: hidden;
  }
  .card--front { left: 221px; }
  .card--back { left: 616px; }

  .brand-name {
    position: absolute;
    color: var(--ink);
    font-weight: 400;
    letter-spacing: 0.5px;
    display: flex; align-items: center; gap: 8px;
    line-height: 1;
  }
  .brand-name .mark {
    display: inline-block; background: var(--tile-green-deep);
  }
  .card--front .brand-name { left: 26px; top: 42px; font-size: 30px; }
  .card--front .brand-name .mark { width: 14px; height: 14px; }
  .card--back .brand-name { left: 30px; top: 138px; font-size: 38px; }
  .card--back .brand-name .mark { width: 16px; height: 16px; }

  .website {
    position: absolute; left: 151px; top: 47px;
    font-size: 10px; color: var(--ink-soft);
  }

  .tile { position: absolute; }
  .tile--building-blue { left: 167px; top: 75px; width: 49px; height: 49px;
    background: linear-gradient(160deg, #4fc0ee, var(--tile-blue)); }
  .tile--building-green { left: 267px; top: 75px; width: 49px; height: 49px;
    background: linear-gradient(160deg, #7cc77a, var(--tile-green)); }
  .tile--sign-green { left: 217px; top: 125px; width: 49px; height: 49px;
    background: linear-gradient(160deg, #86c984, #4ea84f); }
  .tile--tower-blue { left: 317px; top: 125px; width: 49px; height: 49px;
    background: linear-gradient(160deg, #5cc4ef, #2b8fc9); }
  .tile--hands-grey { left: 67px; top: 176px; width: 99px; height: 48px;
    background: linear-gradient(120deg, #c9c9c9, var(--tile-grey) 60%, #6b6b6b); }
  .tile--water-blue { left: 168px; top: 176px; width: 98px; height: 48px;
    background: linear-gradient(120deg, #3fb2e6, var(--tile-blue-deep)); }
  .tile--leaves-green { left: 268px; top: 176px; width: 98px; height: 48px;
    background: linear-gradient(120deg, #7ccb5e, var(--tile-green-deep)); }

  .divider {
    position: absolute; left: 190px; top: 61px;
    width: 1px; height: 124px; background: var(--accent-blue);
  }
  .contact { position: absolute; left: 212px; top: 60px; }
  .contact .person {
    font-size: 14px; font-weight: 700; color: var(--ink); line-height: 16px;
  }
  .contact .role {
    font-size: 14px; font-weight: 600; color: var(--accent-blue); line-height: 16px;
  }
  .contact .details {
    margin-top: 19px; font-size: 10px; line-height: 13px; color: var(--ink-soft);
    font-style: normal;
  }
  .contact .details b { font-weight: 700; color: var(--ink); }
</style>
</head>
<body>
<main class="stage">
  <section class="card card--front" aria-label="Card front">
    <div class="brand-name"><span class="mark"></span>Vexel</div>
    <div class="website">www.vexel-example.com.au</div>
    <div class="tile tile--building-blue" role="img" aria-label="Photo of an apartment building tinted blue"></div>
    <div class="tile tile--building-green" role="img" aria-label="Photo of a residential building tinted green"></div>
    <div class="tile tile--sign-green" role="img" aria-label="Photo of a building sign tinted green"></div>
    <div class="tile tile--tower-blue" role="img" aria-label="Photo of an office tower tinted blue"></div>
    <div class="tile tile--hands-grey" role="img" aria-label="Black and white photo of hands working on plans"></div>
    <div class="tile tile--water-blue" role="img" aria-label="Photo of rippling blue water"></div>
    <div class="tile tile--leaves-green" role="img" aria-label="Photo of green leaves"></div>
  </section>

  <section class="card card--back" aria-label="Card back">
    <div class="brand-name"><span class="mark"></span>Vexel</div>
    <div class="divider"></div>
    <div class="contact">
      <div class="person">Joel Harcastle</div>
      <div class="role">Director</div>
      <address class="details">
        Vexel Consultants Pty Ltd<br>
        Fernhollow first floor<br>
        Tamber Street<br>
        Elmsworth VIC 3988 Australia<br>
        <b>P</b>+61 03 9555 0187<br>
        <b>E</b>mail@vexel-example.com.au
      </address>
    </div>
  </section>
</main>
</body>
</html>
```